KVRo Business Cards

We need a business card design. We are a Technology (Audio Visual) design, sales and installation company. Looking for a double sided design, clean

Contact Information for Business Card

Clean, modern look, 2 sided

Font styles to use
Sans Serif

```html
<!DOCTYPE html>
<html lang="en">
<head>
<meta charset="utf-8">
<title>KVRo Business Card</title>
<link rel="stylesheet" href="https://fonts.googleapis.com/css2?family=Poppins:wght@700&family=Open+Sans:wght@400;600&family=Alegreya+Sans:wght@400&display=swap">
<style>
  :root {
    --page: #ffffff;
    --card-dark: #0d1011;
    --ink: #111111;
    --logo-light: #ffffff;
    --accent: #f7871f;
    --band: #b1bcbc;
    --border: #111111;
  }
  * { margin: 0; padding: 0; box-sizing: border-box; }
  html, body {
    width: 966px; height: 1200px; overflow: hidden;
    background: var(--page);
  }
  .canvas { position: relative; width: 966px; height: 1200px; }

  .card-front {
    position: absolute; left: 111px; top: 99px;
    width: 748px; height: 429px;
    background: var(--card-dark);
    display: flex; align-items: center; justify-content: center;
  }
  .brand {
    display: flex; align-items: center; gap: 12px;
    margin-top: -20px;
  }
  .brand-name {
    font-family: "Poppins", sans-serif; font-weight: 700;
    font-size: 96px; line-height: 1; letter-spacing: -2px;
    color: var(--logo-light);
  }
  .brand-dot {
    width: 18px; height: 18px; background: var(--accent);
    align-self: flex-start; margin-top: 10px;
  }

  .card-back {
    position: absolute; left: 111px; top: 661px;
    width: 748px; height: 428px;
    background: var(--page);
    border: 2px solid var(--border);
    overflow: hidden;
  }
  .holder {
    position: absolute; left: 245px; top: 145px;
    color: var(--accent);
  }
  .holder-name {
    display: flex; align-items: center; gap: 14px;
    font-family: "Open Sans", sans-serif; font-weight: 600;
    font-size: 25px; line-height: 1;
  }
  .holder-role {
    font-family: "Open Sans", sans-serif; font-weight: 400;
    font-size: 18px; margin: 10px 0 0 53px;
  }
  .contact {
    position: absolute; display: flex; align-items: center;
    font-family: "Alegreya Sans", sans-serif; font-size: 23px;
    color: var(--ink); line-height: 1; white-space: nowrap;
  }
  .contact svg { flex: none; }
  .contact .sep { margin: 0 16px 0 12px; }
  .contact-phone { left: 96px; top: 290px; }
  .contact-email { left: 393px; top: 290px; }
  .contact-web { left: 207px; top: 335px; }
  .address-band {
    position: absolute; left: 0; right: 0; bottom: 0; height: 52px;
    background: var(--band);
  }
  .contact-address { left: 96px; top: 12px; }
</style>
</head>
<body>
<main class="canvas">
  <section class="card-front">
    <div class="brand">
      <span class="brand-name">KVRo</span>
      <span class="brand-dot"></span>
    </div>
  </section>

  <section class="card-back">
    <div class="holder">
      <p class="holder-name">
        <svg width="24" height="26" viewBox="0 0 24 26" fill="none" stroke="currentColor" stroke-width="2.4">
          <circle cx="13" cy="8" r="6"/><path d="M9 13 L3 24"/>
        </svg>
        Arin Pellakar
      </p>
      <p class="holder-role">chief executive officer</p>
    </div>

    <p class="contact contact-phone">
      <svg width="18" height="26" viewBox="0 0 18 26" fill="none" stroke="currentColor" stroke-width="2">
        <rect x="2" y="2" width="14" height="22" rx="2"/><path d="M5 9v3"/>
      </svg>
      <span class="sep">:</span>(000)000-123
    </p>
    <p class="contact contact-email">
      <svg width="26" height="20" viewBox="0 0 26 20" fill="none" stroke="currentColor" stroke-width="2.2">
        <rect x="2" y="2" width="22" height="16"/><path d="M2 2 L13 11 L24 2"/>
      </svg>
      <span class="sep">:</span>email@your.com
    </p>
    <p class="contact contact-web">
      <svg width="24" height="24" viewBox="0 0 24 24" fill="none" stroke="currentColor" stroke-width="2">
        <circle cx="12" cy="12" r="10"/><ellipse cx="12" cy="12" rx="4" ry="10"/><path d="M2 12h20M4 7h16M4 17h16"/>
      </svg>
      <span class="sep">:</span>www.yourcompany.com
    </p>

    <div class="address-band">
      <p class="contact contact-address">
        <svg width="26" height="22" viewBox="0 0 26 22" fill="none" stroke="currentColor" stroke-width="2.4">
          <path d="M3 20 V11 L13 3 L23 11 V20"/>
        </svg>
        <span class="sep">:</span>Address line 1, Address line 2, Address line 3
      </p>
    </div>
  </section>
</main>
</body>
</html>
```